Spring 2026 Deck Construction Direct Mail Flier

The logo files I will include were named "maple ridge fixers" by the digital artist. However, my company is called Maple Ridge Yardworks (That was not a typo. There is no space between "home" and "service") If you'd like to experiment with color modification of the logo to make it fit better with designs you come up with, please be my guest.

I need a 6"x12" flier design to market my deck construction business. The expected goal is to get phone calls and book appointments for the upcoming Spring 2026 construction season. The call to action being something along the lines of "Call now; Appointments are going fast!"

My target audience is upper middle class (annual household income $100,000 - $200,000) families of 3-5 in the capital region of New York state, US. Houses are most commonly either vinyl sided, or sometimes a combination of vinyl siding and brick. The ideal flier design will feature this type of house. Also most houses in my target area have nice lawns with mulched gardens as well.

I prefer designs with more sweeping, gradual curves than sharp square edges and corners, though some squares and corners are ok. I like designs with pallets consisting of blue, red, green, black, gray. I do not like purple, pink, yellow, or orange.

If it's possible and will fit, it would be nice to have images of pressure treated lumber, western cedar decking, and composite decking, so that customers understand I can provide any of the three. Also listing them out would be great.

I prefer designs that are more visual than text-based. On at least one side the dominant element should be a visual of a large composite or cedar deck. An image somewhere - wherever it can fit - of a small (10'x14' or so), basic deck of pressure treated lumber would be ideal as well so that potential clients know I will build those. Also I would like some element, on either side, that creates a sense of urgency by drawing the eye to text along the lines of "2026 appointments are filling fast. Book your free consultation today!"

Selling points:
- Veteran owned and operated
- Hometown feel
- Personal service
- Satisfaction guaranteed

I will use the Northfield Parcel Bureau's "Bright Lane Route Mailer" (BLRM) service to deliver these, so on either the front or back there should be a small amount of reserved space in the top right corner for the NFPB's required markings (see https://www.larkstonepromo.com/products/plumber-fixit-blrm-postcard?variant=17305529816 for an example of the amount of space required). It's ok if there is imagery there and it gets covered up by the NFPB markings, it just shouldn't be anything important. You do not have to include the NFPB markings themselves. My print guy will do that when I pass him this design.

A final note on this; I've mentioned Spring 2026 several times. But I do not want the design to be relevant only for Spring. I'd like to use the design throughout the year so please no hard references to Spring that will make the flier seem out of place in the fall.

Thank you very much. I appreciate your time.

```html
<!DOCTYPE html>
<html lang="en">
<head>
<meta charset="utf-8">
<title>Maple Ridge Yardworks – Custom Deck Mailer</title>
<link rel="stylesheet" href="https://fonts.googleapis.com/css2?family=Inter:wght@400;500&family=Playfair+Display:ital,wght@0,800;1,600&family=Poppins:wght@400;500;600;700;800&display=swap">
<style>
  :root {
    --navy: #14325c;
    --red: #c0242b;
    --orange: #d0692a;
    --ink: #111111;
    --green: #3a9a45;
    --paper: #ffffff;
    --canvas: #ebe9e9;
    --text: #222a35;
  }
  * { box-sizing: border-box; margin: 0; padding: 0; }
  html, body { width: 1200px; height: 1130px; overflow: hidden; background: var(--canvas); }
  body { position: relative; font-family: "Poppins", sans-serif; color: var(--text); }

  .card { position: absolute; left: 137px; width: 926px; height: 463px; background: var(--paper); overflow: hidden; }
  .card--front { top: 46px; }
  .card--back { top: 565px; }

  .front-art { position: absolute; inset: 0; }

  .brand-seal {
    position: absolute; width: 150px; height: 150px; border-radius: 50%;
    background: var(--paper); border: 4px solid var(--navy);
    display: flex; align-items: center; justify-content: center; text-align: center;
    font-family: "Poppins", sans-serif; font-weight: 700; color: var(--navy);
    font-size: 17px; line-height: 1.2; letter-spacing: 0.5px; text-transform: uppercase;
  }
  .card--front .brand-seal { left: 23px; top: 18px; }
  .card--back .brand-seal { left: 29px; top: 25px; width: 134px; height: 134px; font-size: 15px; }

  .postage-box { position: absolute; left: 835px; top: 21px; width: 61px; height: 57px; border: 1.5px solid var(--ink); }

  .headline { position: absolute; right: 29px; top: 38px; text-align: right; white-space: nowrap; }
  .headline__lead { font-family: "Playfair Display", serif; font-style: italic; font-weight: 600; font-size: 46px; color: var(--ink); line-height: 1; margin-right: 160px; }
  .headline__main { font-family: "Playfair Display", serif; font-weight: 800; font-size: 64px; color: var(--navy); line-height: 1; margin-top: 2px; letter-spacing: -0.5px; }
  .headline__sub { font-family: "Poppins", sans-serif; font-weight: 700; font-size: 57px; color: var(--ink); line-height: 1.05; letter-spacing: -1px; }

  .urgency-tab {
    position: absolute; left: 650px; top: 220px; width: 276px; height: 77px;
    background: var(--red); border-top-left-radius: 70px 77px;
    color: var(--paper); text-align: right; padding: 11px 29px 0 0;
    font-size: 21px; font-weight: 500; line-height: 1.2; white-space: nowrap;
  }

  .phone-line { position: absolute; right: 29px; top: 312px; display: flex; align-items: center; gap: 10px; font-weight: 700; font-size: 50px; color: var(--ink); letter-spacing: -1px; line-height: 1; white-space: nowrap; }
  .phone-line svg { width: 38px; height: 42px; }

  .perks { position: absolute; left: 519px; top: 372px; display: grid; grid-template-columns: 207px auto; row-gap: 7px; list-style: none; font-family: "Inter", sans-serif; font-size: 13.5px; color: var(--ink); white-space: nowrap; }
  .perks li { display: flex; align-items: center; gap: 7px; line-height: 16px; }
  .tick-box { width: 16px; height: 16px; flex: none; }

  .consult-bar {
    position: absolute; left: 0; right: 0; bottom: 0; height: 36px;
    color: var(--paper); font-weight: 700; font-size: 17px; text-align: right;
    padding: 7px 29px 0 0; letter-spacing: 0.2px; white-space: nowrap;
    z-index: 0; isolation: isolate;
  }
  .consult-bar svg { position: absolute; inset: 0; z-index: -1; }

  .side-tag { position: absolute; left: 879px; top: 0; width: 47px; height: 70px; background: var(--red); }
  .side-tag__label { position: absolute; left: 842px; top: 15px; width: 66px; height: 31px; background: var(--navy); color: var(--paper); font-size: 19px; font-weight: 500; text-align: center; line-height: 31px; }

  .back-title { position: absolute; left: 206px; top: 32px; font-weight: 700; font-size: 46px; line-height: 1.15; color: var(--navy); letter-spacing: -0.5px; white-space: nowrap; }
  .title-rule { position: absolute; left: 206px; top: 145px; width: 720px; height: 2px; background: var(--navy); }

  .material { position: absolute; top: 170px; width: 206px; height: 219px; border: 5px solid; border-radius: 24px; overflow: hidden; background: var(--paper); }
  .material--pt { left: 30px; border-color: var(--navy); }
  .material--cedar { left: 247px; border-color: var(--orange); }
  .material--composite { left: 465px; border-color: var(--red); }
  .material__photo { height: 156px; }
  .material__caption { text-align: center; font-family: "Inter", sans-serif; font-size: 13.5px; line-height: 1.3; color: var(--ink); padding-top: 8px; white-space: nowrap; }

  .back-divider { position: absolute; left: 689px; top: 171px; width: 1.5px; height: 216px; background: var(--navy); }

  .trust { position: absolute; left: 700px; top: 172px; width: 214px; text-align: center; color: var(--navy); white-space: nowrap; }
  .trust__word { font-weight: 600; font-size: 29px; line-height: 32px; }
  .trust__phone { font-weight: 500; font-size: 22px; line-height: 30px; display: flex; align-items: center; justify-content: center; gap: 3px; letter-spacing: -0.3px; }
  .trust__phone svg { width: 18px; height: 18px; }
  .trust-rule { position: absolute; left: 705px; top: 247px; width: 190px; height: 1.5px; background: var(--navy); }

  .trust-list { position: absolute; left: 705px; top: 267px; list-style: none; font-family: "Inter", sans-serif; font-size: 13.5px; color: var(--ink); white-space: nowrap; }
  .trust-list li { display: flex; align-items: center; gap: 6px; height: 26.5px; }
  .trust-list svg { width: 20px; height: 20px; flex: none; }

  .slots-band { position: absolute; left: 0; bottom: 0; width: 689px; height: 56px; background: var(--red); color: var(--paper); font-weight: 700; font-size: 25px; line-height: 56px; padding-left: 29px; letter-spacing: -0.3px; white-space: nowrap; }
  .address-band { position: absolute; right: 0; bottom: 0; width: 237px; height: 56px; background: var(--navy); color: var(--paper); font-family: "Inter", sans-serif; font-size: 11.5px; line-height: 1.4; padding: 12px 0 0 15px; white-space: nowrap; }
</style>
</head>
<body>

<section class="card card--front" aria-label="Mailer front">
  <svg class="front-art" viewBox="0 0 926 463" preserveAspectRatio="none">
    <defs>
      <linearGradient id="houseScene" x1="0" y1="0" x2="0" y2="1">
        <stop offset="0" stop-color="#e9ecef"/>
        <stop offset="0.35" stop-color="#d7dadd"/>
        <stop offset="0.6" stop-color="#b88a5e"/>
        <stop offset="0.78" stop-color="#6e4e35"/>
        <stop offset="1" stop-color="#5d9a3c"/>
      </linearGradient>
    </defs>
    <path d="M0,463 V0 H565 C520,140 485,300 463,463 Z" fill="url(#houseScene)" role="img" aria-label="Photo of a vinyl-sided and brick two-storey home with a large wood-tone deck, railings and stairs, mulched garden beds and a green lawn"/>
    <path d="M0,0 H480 C300,20 90,120 0,285 Z" fill="var(--navy)"/>
    <path d="M0,285 C90,120 300,20 480,0 H560 C340,30 100,150 0,330 Z" fill="var(--red)"/>
  </svg>

  <div class="brand-seal">Maple Ridge<br>Yardworks</div>
  <div class="postage-box" aria-hidden="true"></div>

  <div class="headline">
    <p class="headline__lead">Beautiful</p>
    <p class="headline__main">Custom Decks</p>
    <p class="headline__sub">Built to Last</p>
  </div>

  <div class="urgency-tab">2026 Appointments<br>Are Filling Fast!</div>

  <div class="phone-line">
    <svg viewBox="0 0 24 24" aria-hidden="true"><path fill="var(--navy)" d="M6.6 2.2c.6-.4 1.4-.2 1.8.4l2.1 3.4c.4.6.2 1.3-.3 1.7L8.6 8.9c-.3.2-.4.6-.2 1 1.2 2.4 2.9 4.7 5.1 6.4.3.2.7.2 1-.1l1.4-1.4c.5-.5 1.3-.5 1.8 0l2.9 2.7c.5.5.5 1.3 0 1.8l-1.7 1.7c-.9.9-2.2 1.2-3.4.7C10 19.2 5.1 13.8 3 7.5c-.4-1.2 0-2.5 1-3.3z"/></svg>
    <span>(518) 555-0147</span>
  </div>

  <ul class="perks">
    <li><svg class="tick-box" viewBox="0 0 16 16"><rect x="1" y="1" width="14" height="14" rx="2" fill="none" stroke="var(--green)" stroke-width="1.8"/><path d="M4 8.2l3 3 6-7" fill="none" stroke="var(--green)" stroke-width="2.2" stroke-linecap="round"/></svg>Veteran Owned &amp; Operated</li>
    <li><svg class="tick-box" viewBox="0 0 16 16"><rect x="1" y="1" width="14" height="14" rx="2" fill="none" stroke="var(--green)" stroke-width="1.8"/><path d="M4 8.2l3 3 6-7" fill="none" stroke="var(--green)" stroke-width="2.2" stroke-linecap="round"/></svg>Personal Service</li>
    <li><svg class="tick-box" viewBox="0 0 16 16"><rect x="1" y="1" width="14" height="14" rx="2" fill="none" stroke="var(--green)" stroke-width="1.8"/><path d="M4 8.2l3 3 6-7" fill="none" stroke="var(--green)" stroke-width="2.2" stroke-linecap="round"/></svg>Personal Service</li>
    <li><svg class="tick-box" viewBox="0 0 16 16"><rect x="1" y="1" width="14" height="14" rx="2" fill="none" stroke="var(--green)" stroke-width="1.8"/><path d="M4 8.2l3 3 6-7" fill="none" stroke="var(--green)" stroke-width="2.2" stroke-linecap="round"/></svg>Satisfaction Guaranteed</li>
  </ul>

  <div class="consult-bar">
    <svg viewBox="0 0 926 36" preserveAspectRatio="none" aria-hidden="true"><path d="M490,0 H926 V36 H465 C472,20 480,8 490,0 Z" fill="var(--navy)"/></svg>
    BOOK YOUR FREE CONSULTATION TODAY!
  </div>
</section>

<section class="card card--back" aria-label="Mailer back">
  <div class="side-tag" aria-hidden="true"></div>
  <div class="side-tag__label">Back</div>

  <div class="brand-seal">Maple Ridge<br>Yardworks</div>

  <h1 class="back-title">Transform Your<br>Backyard with a Custom Deck</h1>
  <div class="title-rule"></div>

  <figure class="material material--pt">
    <div class="material__photo" role="img" aria-label="Photo of a small pressure treated lumber deck with wood railings beside a white house" style="background:linear-gradient(180deg,#cfd6d2 0%,#7e8f62 30%,#b8773e 45%,#d79a5c 100%)"></div>
    <figcaption class="material__caption">Pressure Treated Lumber:<br>Durable &amp; Affordable</figcaption>
  </figure>
  <figure class="material material--cedar">
    <div class="material__photo" role="img" aria-label="Photo of a western cedar deck with warm-toned boards and railings overlooking a lawn" style="background:linear-gradient(180deg,#5c8a45 0%,#7ea456 30%,#b46a35 45%,#d08a4e 100%)"></div>
    <figcaption class="material__caption">Western Cedar Decking:<br>Natural Beauty</figcaption>
  </figure>
  <figure class="material material--composite">
    <div class="material__photo" role="img" aria-label="Photo of a gray composite deck with dark railings overlooking trees" style="background:linear-gradient(180deg,#dfe5ea 0%,#8ea07a 30%,#54585c 45%,#8b8d8f 100%)"></div>
    <figcaption class="material__caption">Composite Decking:<br>Low Maintenance</figcaption>
  </figure>

  <div class="back-divider"></div>

  <div class="trust">
    <p class="trust__word">Trust</p>
    <p class="trust__phone"><svg viewBox="0 0 24 24" aria-hidden="true"><path fill="var(--navy)" d="M6.6 2.2c.6-.4 1.4-.2 1.8.4l2.1 3.4c.4.6.2 1.3-.3 1.7L8.6 8.9c-.3.2-.4.6-.2 1 1.2 2.4 2.9 4.7 5.1 6.4.3.2.7.2 1-.1l1.4-1.4c.5-.5 1.3-.5 1.8 0l2.9 2.7c.5.5.5 1.3 0 1.8l-1.7 1.7c-.9.9-2.2 1.2-3.4.7C10 19.2 5.1 13.8 3 7.5c-.4-1.2 0-2.5 1-3.3z"/></svg>(518)555-0147</p>
  </div>
  <div class="trust-rule"></div>

  <ul class="trust-list">
    <li><svg viewBox="0 0 20 20"><rect x="1" y="4" width="14" height="14" fill="none" stroke="var(--navy)" stroke-width="1.6"/><path d="M4 10l4 4 10-12" fill="none" stroke="var(--navy)" stroke-width="2.2" stroke-linecap="round"/></svg>Veteran Owned &amp; Operated</li>
    <li><svg viewBox="0 0 20 20"><rect x="1" y="4" width="14" height="14" fill="none" stroke="var(--navy)" stroke-width="1.6"/><path d="M4 10l4 4 10-12" fill="none" stroke="var(--navy)" stroke-width="2.2" stroke-linecap="round"/></svg>Local Hometown Company</li>
    <li><svg viewBox="0 0 20 20"><rect x="1" y="4" width="14" height="14" fill="none" stroke="var(--navy)" stroke-width="1.6"/><path d="M4 10l4 4 10-12" fill="none" stroke="var(--navy)" stroke-width="2.2" stroke-linecap="round"/></svg>One-on-One Personal Service</li>
  </ul>

  <div class="slots-band">LIMITED 2026 BUILD SLOTS AVAILABLE — Call Today!</div>
  <div class="address-band">Maple Ridge Yardworks,<br>Capital Region of New York State, USA</div>
</section>

</body>
</html>
```